brightloom corporate presentation

We have a wireframe presentation with 18 slides to be implemented in Google slides (powerpoint optional although we would rather prefer Google slides). Please, be creative and don't take the examples in the wireframe as literal. We also provide the following:

- Color palet
- brightloom Logos
- Slide wireframe
- slide reference for slide number 5.
- Flyer
- Partner logos

You can find all the materials here: https://files.kelvoria.example/share/7qpW3mRtX9vLa2Nc8ZyHbD4FgK1sJe6Uo

```html
<!DOCTYPE html>
<html lang="en">
<head>
<meta charset="utf-8">
<title>brightloom corporate presentation</title>
<link href="https://fonts.googleapis.com/css2?family=Carlito:ital,wght@0,400;0,700;1,400&display=swap" rel="stylesheet">
<style>
  :root {
    --page: #ffffff;
    --navy: #0a1628;
    --teal: #2bb3a3;
    --magenta: #7a0f7c;
    --plum: #3a0e4f;
    --deep: #1a1240;
    --white: #ffffff;
    --line: #2a7f78;
  }
  * { margin: 0; padding: 0; box-sizing: border-box; }
  html, body {
    width: 1200px; height: 1200px; overflow: hidden;
    background: var(--page);
    font-family: "Carlito", "Calibri", sans-serif;
    color: var(--white);
  }
  .deck { position: relative; width: 1200px; height: 1200px; }
  .slide {
    position: absolute; left: 289px; width: 622px; height: 350px;
    overflow: hidden; background: var(--navy);
  }
  .slide--cover { top: 63px; }
  .slide--quote { top: 425px; }
  .slide--about { top: 787px; }

  .accent { color: var(--teal); font-weight: 700; }

  /* brand wordmark */
  .brand { position: absolute; display: flex; align-items: center; font-weight: 700; color: var(--white); }
  .brand__dot { background: var(--teal); }
  .brand--large { left: 406px; top: 40px; font-size: 34px; gap: 7px; }
  .brand--large .brand__dot { width: 18px; height: 18px; }
  .brand--small { left: 561px; top: 328px; font-size: 9px; gap: 3px; }
  .brand--small .brand__dot { width: 5px; height: 5px; }

  /* cover */
  .cover__glow {
    position: absolute; inset: 0;
    background:
      radial-gradient(ellipse 200px 110px at 330px 340px, rgba(0,170,150,0.95), transparent 75%),
      radial-gradient(ellipse 170px 110px at 600px 300px, rgba(140,0,130,0.95), transparent 75%),
      radial-gradient(ellipse 150px 90px at 30px 360px, rgba(80,60,170,0.9), transparent 80%),
      radial-gradient(ellipse 220px 80px at 180px 330px, rgba(20,110,160,0.8), transparent 80%);
  }
  .cover__bar { position: absolute; left: 0; top: 140px; width: 23px; height: 104px; background: var(--plum); }
  .cover__title {
    position: absolute; left: 37px; top: 145px;
    font-size: 36px; line-height: 47px; font-weight: 400;
  }
  .cover__meta {
    position: absolute; right: 33px; top: 300px;
    text-align: right; font-size: 10.5px; line-height: 14px;
  }
  .cover__tab { position: absolute; right: 0; top: 298px; width: 20px; height: 31px; background: #2a1248; }

  /* shared slide chrome */
  .slide__heading {
    position: absolute; left: 29px; top: 21px; font-size: 16.5px;
  }
  .slide__tag { position: absolute; left: 0; top: 19px; width: 15px; height: 26px; }
  .slide__tag--magenta { background: var(--magenta); }
  .slide__tag--teal { background: var(--teal); }
  .rule-v { position: absolute; left: 601px; top: 19px; width: 1px; height: 296px; background: var(--line); }
  .rule-h { position: absolute; left: 16px; top: 334px; width: 536px; height: 1px; background: var(--line); }
  .site {
    position: absolute; left: 604px; top: 166px;
    font-size: 6px; letter-spacing: 2px; color: #9aa3b5;
    transform: rotate(-90deg); transform-origin: left top;
    white-space: nowrap;
  }

  /* quote slide */
  .quote__visual {
    position: absolute; left: 301px; top: 0; width: 255px; height: 251px;
    border-bottom-right-radius: 40px;
    background:
      radial-gradient(circle at 50% 40%, #4fa6e8 0%, #1d4f9a 35%, #142a5c 60%, transparent 75%),
      linear-gradient(180deg, #0b1a3a 0%, #1a2f6a 60%, #6a72b8 85%, #2a2c6a 100%);
  }
  .quote__card {
    position: absolute; left: 68px; top: 117px; width: 419px; height: 176px;
    border-radius: 12px;
    background: linear-gradient(90deg, rgba(90,14,100,0.95), rgba(110,12,110,0.9));
  }
  .quote__text {
    position: absolute; left: 16px; top: 26px; width: 270px;
    font-size: 16px; line-height: 21.8px;
  }
  .quote__source {
    position: absolute; right: 14px; bottom: 8px;
    font-size: 10px; font-style: italic;
  }

  /* about slide */
  .slide--about {
    background: linear-gradient(100deg, #2a1048 0%, #1c1448 40%, #10163a 75%, #121a44 100%);
  }
  .about__waves {
    position: absolute; left: 160px; top: 0; width: 462px; height: 260px;
    background: radial-gradient(ellipse 230px 120px at 60% 45%, rgba(120,140,210,0.18), transparent 75%);
  }
  .about__title {
    position: absolute; left: 65px; top: 100px;
    font-size: 37px; line-height: 46px; font-weight: 700;
  }
  .about__underline { position: absolute; left: 65px; top: 202px; width: 113px; height: 3px; background: var(--teal); }
  .about__lede {
    position: absolute; left: 65px; top: 218px; width: 306px;
    font-size: 10px; line-height: 14px;
  }
</style>
</head>
<body>
<main class="deck">

  <section class="slide slide--cover">
    <div class="cover__glow"></div>
    <div class="brand brand--large"><span class="brand__dot"></span>brightloom</div>
    <div class="cover__bar"></div>
    <h1 class="cover__title">Leading <span class="accent">the future</span><br>with <span class="accent">Data</span> and <span class="accent">Intelligence</span></h1>
    <p class="cover__meta">Marco Ferrel<br>Madrid, 11 Junio 2025</p>
    <div class="cover__tab"></div>
  </section>

  <section class="slide slide--quote">
    <div class="slide__tag slide__tag--magenta"></div>
    <h2 class="slide__heading">The future is <span class="accent">now</span></h2>
    <div class="quote__visual" role="img" aria-label="Glowing digital globe above a futuristic city skyline"></div>
    <figure class="quote__card">
      <blockquote class="quote__text">"Generative AI has the potential to add trillions of dollars in value to the global economy and accelerate productivity growth for individuals, businesses, and the economy as a whole."</blockquote>
      <figcaption class="quote__source">Halvorsen &amp; Partners</figcaption>
    </figure>
    <div class="rule-v"></div>
    <div class="site">www.brightloom.com</div>
    <div class="rule-h"></div>
    <div class="brand brand--small"><span class="brand__dot"></span>brightloom</div>
  </section>

  <section class="slide slide--about">
    <div class="about__waves" role="img" aria-label="Flowing dotted particle waves"></div>
    <div class="slide__tag slide__tag--teal"></div>
    <h2 class="slide__heading">About Us</h2>
    <h1 class="about__title">Data Analytics<br>&amp; AI for Nonconformists</h1>
    <div class="about__underline"></div>
    <p class="about__lede">We are a leading Professional Services company specialized in the design and implementation of cutting edge technologies in Cloud, Data Analytics &amp; AI.</p>
    <div class="rule-v"></div>
    <div class="site">www.brightloom.com</div>
    <div class="rule-h"></div>
    <div class="brand brand--small"><span class="brand__dot"></span>brightloom</div>
  </section>

</main>
</body>
</html>
```